Website Design for a "Talent Recruitment Agency"

We are looking for a website design for the website of our "Talent Recruitment Agency"; which is called "Crestway Hub".
Our recruitment website "Crestway Hub" will be focusing on: "Crestway Hub: Linking People & Firms in Switzerland"; which means our target audience is two-folded:
(i) TALENT - that is currently residing in- or outside of Switzerland, and is open for and interested in the "Swiss Job Market".
(ii) COMPANIES - that are looking for talent for specific job vacancies in Switzerland.
With our "Crestway Hub" approach we inted to focus on Membership & Partnership:
(a)"Membership"(TALENT)
and
(b)"Partnership"(COMPANIES)
Some of the competitor sites we like are:
• www.plimora42.dk
• www.qelvo.ch
• www.brandolix.ch/en
A sitemap example of our website is attached.
Also attached is a "Crestway Hub" logo in .eps format and one in .jpeg format.
We very much look forward to receive your creative ideas.
Best regards,
Crestway Hub
Crestway Hub: Linking People & Firms in Switzerland.
Website: crestwayhub.ch - Twitter: CrestwayHubCH
Target Market(s)
(i) TALENT (with around 0-10 years of working experience), currently residing in- or outside of Switzerland, but eligible to work in Switzerland.
(ii) COMPANIES (national or international) that are based in Switzerland.
Industry/Entity Type
Recruitment

```html
<!DOCTYPE html>
<html lang="en">
<head>
<meta charset="utf-8">
<title>Crestway Hub – Linking People &amp; Firms in Switzerland</title>
<link rel="stylesheet" href="https://fonts.googleapis.com/css2?family=Open+Sans:wght@400;600;700&family=Questrial&display=swap">
<style>
:root{
  --blue:#1a7fc1;
  --blue-dark:#0f6aa6;
  --footer-blue:#0f77b8;
  --footer-bottom:#0b5f96;
  --orange:#f07b1d;
  --orange-dark:#d9690f;
  --text:#555;
  --muted:#7a7a7a;
  --rule:#dcdcdc;
  --band:#f2f2f2;
  --white:#fff;
}
*{box-sizing:border-box;margin:0;padding:0}
html,body{width:1200px;height:2311px;overflow:hidden}
body{position:relative;background:var(--white);font-family:"Open Sans",Arial,sans-serif;color:var(--text)}
.abs{position:absolute}
.top-stripe{left:0;top:0;width:1200px;height:6px;background:var(--orange)}

/* header */
.brand{left:69px;top:72px;display:flex;align-items:center;gap:12px}
.brand-dot{width:54px;height:54px;border-radius:50%;background:var(--orange)}
.brand-name{font-family:"Questrial",sans-serif;font-size:40px;font-weight:700;color:var(--blue)}
.lang{right:53px;top:30px;font-size:13px;color:var(--muted);display:flex;align-items:center;gap:6px}
.flag{width:16px;height:16px}
.call{right:53px;top:66px;font-family:"Questrial",sans-serif;font-size:18px;color:var(--orange);display:flex;align-items:center;gap:6px}
.phone-top{right:53px;top:89px;font-family:"Questrial",sans-serif;font-size:19px;color:var(--blue);letter-spacing:1px}
.social{right:53px;top:127px;display:flex;gap:8px}
.social span{width:26px;height:26px;border-radius:50%;display:block}

/* nav */
.nav{left:48px;top:180px;width:1104px;height:40px;background:linear-gradient(#2a8fd0,#157bbd);border-radius:3px;display:flex;align-items:center}
.nav a{color:var(--white);text-decoration:none;font-family:"Questrial",sans-serif;font-size:16px;letter-spacing:1px;height:40px;line-height:40px;padding:0 30px;border-right:1px solid rgba(0,0,0,.15)}
.nav a:first-child{padding-left:35px}
.nav a:nth-child(7){border-right:none}
.search{position:absolute;right:10px;top:7px;width:185px;height:26px;background:var(--white);border-radius:2px;font-size:11px;color:#999;line-height:26px;padding-left:8px}
.search svg{position:absolute;right:8px;top:8px}

/* hero */
.grey-band{left:0;top:624px;width:1200px;height:450px;background:var(--band)}
.hero{left:48px;top:234px;width:1104px;height:407px;background:linear-gradient(90deg,#eef5fb,#dfeaf5);border-bottom:3px solid var(--blue)}
.hero-photo{position:absolute;left:505px;top:0;width:599px;height:404px;background:linear-gradient(160deg,#e7eef6,#c8d5e3 60%,#b7c4d4)}
.hero-title{position:absolute;left:83px;top:46px;font-family:"Questrial",sans-serif;font-size:28px;line-height:28px;color:var(--blue);letter-spacing:1px;width:420px}
.hero-title em{font-style:normal;color:var(--orange)}
.hero-copy{position:absolute;left:83px;top:118px;width:385px;font-size:14px;line-height:21px;color:var(--text)}
.hero-copy p+p{margin-top:21px}
.btn{display:inline-block;background:var(--orange);color:var(--white);border:1px solid var(--orange-dark);font-size:14px}
.hero .btn{position:absolute;left:83px;top:310px;padding:6px 13px}

/* section headings */
.section-head{font-family:"Questrial",sans-serif;font-size:21px;letter-spacing:1px;color:var(--blue);border-bottom:1px solid var(--rule);padding-bottom:10px}
.section-head em{font-style:normal;color:var(--orange)}

/* welcome */
.welcome-head{left:85px;top:701px;width:1033px}
.welcome-visual{left:85px;top:764px;width:410px;height:230px;border:3px solid #d2d2d2;background:linear-gradient(#f6f9fc,#e4ecf4);display:flex;align-items:center;justify-content:center;gap:10px}
.welcome-visual .brand-dot{width:40px;height:40px}
.welcome-visual .brand-name{font-size:26px}
.welcome-copy{left:544px;top:772px;width:563px;font-size:15px;line-height:21px;text-align:justify}
.welcome-copy p+p{margin-top:21px}

/* info */
.info-head{left:85px;top:1147px;width:1033px}
.dots{left:1068px;top:1161px;display:flex;gap:6px}
.dots span{width:10px;height:10px;border-radius:50%;background:var(--blue)}
.dots span:first-child{background:var(--orange)}
.card{top:1221px;width:316px}
.card-photo{height:209px;border:3px solid #d4d4d4}
.card h3{font-family:"Questrial",sans-serif;font-weight:400;font-size:19px;color:var(--blue);letter-spacing:1px;margin-top:13px}
.card p{font-size:12.5px;line-height:17px;margin-top:6px;text-align:justify;letter-spacing:.2px}
.card .btn{font-size:11px;padding:5px 16px;margin-top:20px}

/* partners */
.partners{left:0;top:1723px;width:1200px;height:165px;background:var(--band);display:flex;align-items:center;justify-content:center;gap:58px}
.partners span{width:140px;height:36px;border-radius:4px;background:#cfcfcf;display:block}

/* footer */
.footer{left:0;top:1888px;width:1200px;height:382px;background:var(--footer-blue);color:var(--white)}
.footer h4{font-family:"Questrial",sans-serif;font-weight:400;font-size:16px;letter-spacing:1px;padding-bottom:12px;border-bottom:1px solid rgba(255,255,255,.3)}
.col-events{left:94px;top:37px;width:402px}
.event{display:flex;gap:12px;padding:14px 0 10px 3px;border-bottom:1px solid rgba(255,255,255,.3)}
.event-thumb{width:126px;height:86px;border:3px solid #6aa9d6;background:linear-gradient(#d9dfe6,#a7b2bd);flex:none}
.event h5{font-size:14px;font-weight:700;letter-spacing:.5px}
.event p{font-size:13px;line-height:16px;margin-top:3px}
.event .more{font-size:13px;margin-top:4px;letter-spacing:.5px}
.view-all{font-size:14px;letter-spacing:1px;margin-top:18px;padding-left:5px}
.col-links{left:573px;top:37px;width:208px}
.col-links ul{list-style:none;padding:8px 0 40px 15px;border-bottom:1px solid rgba(255,255,255,.3)}
.col-links li{font-size:14px;line-height:30.5px}
.col-links li::before{content:"›";margin-right:8px}
.col-contact{left:870px;top:37px;width:208px}
.contact-row{display:flex;gap:10px;font-size:14px;line-height:17px;margin-top:18px}
.contact-row svg{flex:none;margin-top:2px}
.footer-brand{position:absolute;left:863px;top:272px;display:flex;align-items:center;gap:8px;opacity:.65}
.footer-brand .brand-dot{width:34px;height:34px;background:var(--white)}
.footer-brand .brand-name{font-size:21px;color:var(--white)}
.footer-bar{left:0;top:2270px;width:1200px;height:41px;background:var(--footer-bottom);color:var(--white);font-size:13px}
.legal{position:absolute;left:98px;top:12px;letter-spacing:.5px}
.legal span{margin:0 14px}
.copyright{position:absolute;left:475px;top:12px;letter-spacing:.5px}
.footer-social{position:absolute;left:953px;top:8px;display:flex;gap:8px}
.footer-social span{width:25px;height:25px;border-radius:50%;background:var(--white);display:block}
</style>
</head>
<body>
<div class="abs top-stripe"></div>

<header>
  <div class="abs brand"><span class="brand-dot"></span><span class="brand-name">Crestway Hub</span></div>
  <div class="abs lang">Select Language:
    <svg class="flag" viewBox="0 0 16 16"><rect width="16" height="16" fill="#e4002b"/><rect x="6.5" y="3" width="3" height="10" fill="#fff"/><rect x="3" y="6.5" width="10" height="3" fill="#fff"/></svg>
  </div>
  <div class="abs call">
    <svg width="15" height="15" viewBox="0 0 24 24"><path fill="#f07b1d" d="M6.6 10.8a15 15 0 0 0 6.6 6.6l2.2-2.2c.3-.3.7-.4 1-.2 1.1.4 2.3.6 3.6.6.6 0 1 .4 1 1V20c0 .6-.4 1-1 1A17 17 0 0 1 3 4c0-.6.4-1 1-1h3.5c.6 0 1 .4 1 1 0 1.3.2 2.5.6 3.6.1.3 0 .7-.2 1z"/></svg>
    Call us:
  </div>
  <div class="abs phone-top">111-111-1111</div>
  <div class="abs social" aria-label="Social links">
    <span style="background:#3ba4d9"></span><span style="background:#3b5a9a"></span><span style="background:#1f73b0"></span><span style="background:#f09a1e"></span>
  </div>
  <nav class="abs nav">
    <a>HOME</a><a>ABOUT</a><a>TALENT</a><a>COMPANIES</a><a>JOBS</a><a>EVENTS</a><a>CONTACT</a>
    <div class="search">Keyword Search
      <svg width="10" height="10" viewBox="0 0 10 10"><circle cx="4" cy="4" r="3" fill="none" stroke="#f07b1d" stroke-width="1.4"/><line x1="6.2" y1="6.2" x2="9.3" y2="9.3" stroke="#f07b1d" stroke-width="1.6"/></svg>
    </div>
  </nav>
</header>

<div class="abs grey-band"></div>

<section class="abs hero">
  <div class="hero-photo" role="img" aria-label="Photo of business people shaking hands, seen from above"></div>
  <h1 class="hero-title" style="font-weight:400">Crestway Hub: <em>Linking</em> People &amp; <em>Firms</em> in Switzerland</h1>
  <div class="hero-copy">
    <p>Lorem ipsum dolor sit amet, consectetur adipiscing elit. Phasellus eget leo leo. Sed adipiscing mi orci, vel ultrices turpis mattis a. Quisque sed eros luctus, euismod ligula et, suscipit dolor.</p>
    <p>Sed adipiscing mi orci, vel ultrices turpis mattis a. Quisque sed eros luctus, euismod ligula et, suscipit dolor ipsum dolor sit amet.</p>
  </div>
  <span class="btn">Read more +</span>
</section>

<section>
  <h2 class="abs section-head welcome-head" style="font-weight:400">WELCOME TO <em>CRESTWAY HUB</em></h2>
  <div class="abs welcome-visual" role="img" aria-label="Network of business people with the Crestway Hub name">
    <span class="brand-dot"></span><span class="brand-name">Crestway Hub</span>
  </div>
  <div class="abs welcome-copy">
    <p>Lorem ipsum dolor sit amet, consectetur adipiscing elit. Phasellus eget leo leo. Sed adipiscing mi orci, vel ultrices turpis mattis a. Quisque sed eros luctus, euismod ligula et, suscipit dolor. Sed suscipit tortor eget leo hendrerit semper. Sed et fermentum erat.</p>
    <p>Curabitur tristique vestibulum bibendum. Quisque eget varius eros. Nunc id laoreet sem. Nullam vulputate fringilla mi sit amet imperdiet. Lorem ipsum dolor sit amet, consectetur adipiscing elit. Pellentesque habitant morbi tristique senectus et netus et malesuada fames ac turpis egestas.</p>
  </div>
</section>

<section>
  <h2 class="abs section-head info-head" style="font-weight:400">USEFUL <em>INFORMATION</em></h2>
  <div class="abs dots"><span></span><span></span><span></span></div>
  <article class="abs card" style="left:85px">
    <div class="card-photo" role="img" aria-label="Photo of a team of young professionals" style="background:linear-gradient(#f4f4f4,#9a9a9a 70%,#3a3a3a)"></div>
    <h3>TALENTS</h3>
    <p>Lorem ipsum dolor sit amet, consectetur adipiscing elit. Curabitur lacinia pretium risus ac euismod.Arabitur lorem lacinia pretium risus ac ipsum dolor sit amet consectetur adi.</p>
    <span class="btn">read more</span>
  </article>
  <article class="abs card" style="left:442px">
    <div class="card-photo" role="img" aria-label="Photo of office towers against a blue sky" style="background:linear-gradient(160deg,#6ea8df,#2f5f94 55%,#172f4c)"></div>
    <h3>COMPANIES</h3>
    <p>Lorem ipsum dolor sit amet, consectetur adipiscing elit. Curabitur lacinia pretium risus ac euismod.Arabitur lorem lacinia pretium risus ac ipsum dolor sit amet consectetur adi.</p>
    <span class="btn">read more</span>
  </article>
  <article class="abs card" style="left:798px">
    <div class="card-photo" role="img" aria-label="Photo of a business meeting at a table" style="background:linear-gradient(#eef0f3,#b9c0c9 60%,#4a5565)"></div>
    <h3>JOB OFFERS</h3>
    <p>Lorem ipsum dolor sit amet, consectetur adipiscing elit. Curabitur lacinia pretium risus ac euismod.Arabitur lorem lacinia pretium risus ac ipsum dolor sit amet consectetur adi.</p>
    <span class="btn">read more</span>
  </article>
</section>

<div class="abs partners" aria-label="Partner companies">
  <span></span><span></span><span></span><span></span><span></span>
</div>

<footer class="abs footer">
  <div class="abs col-events">
    <h4>LATEST EVENTS</h4>
    <div class="event">
      <div class="event-thumb" role="img" aria-label="Photo of a presenter at a flip chart"></div>
      <div><h5>Article Title goes here</h5><p>Lorem ipsum dolor sit amet, consectetur adipiscing elit dolor sit amet sit amet, consectetur.</p><div class="more">Read more +</div></div>
    </div>
    <div class="event">
      <div class="event-thumb" role="img" aria-label="Photo of a presenter at a flip chart"></div>
      <div><h5>Article Title goes here</h5><p>Lorem ipsum dolor sit amet, consectetur adipiscing elit dolor sit amet sit amet, consectetur.</p><div class="more">Read more +</div></div>
    </div>
    <div class="view-all">VIEW ALL ARTICLES</div>
  </div>
  <div class="abs col-links">
    <h4>QUICKLINKS</h4>
    <ul><li>Home</li><li>About</li><li>Talent</li><li>Companies</li><li>Events</li><li>Contact</li></ul>
  </div>
  <div class="abs col-contact">
    <h4>CONTACT INFO</h4>
    <div class="contact-row">
      <svg width="14" height="18" viewBox="0 0 14 18"><path fill="#fff" d="M7 0a7 7 0 0 0-7 7c0 5 7 11 7 11s7-6 7-11a7 7 0 0 0-7-7zm0 10a3 3 0 1 1 0-6 3 3 0 0 1 0 6z"/></svg>
      <span>1344 Your Address<br>Location here, NY<br>Country name</span>
    </div>
    <div class="contact-row">
      <svg width="14" height="12" viewBox="0 0 14 12"><path fill="#fff" d="M0 3c0-2 3-3 7-3s7 1 7 3v1h-3V3H3v1H0zM2 5h10l1 7H1z"/></svg>
      <span>111-111-1111</span>
    </div>
    <div class="contact-row" style="margin-top:32px">
      <svg width="14" height="11" viewBox="0 0 14 11"><rect width="14" height="11" rx="1" fill="#fff"/><path d="M0 1l7 5 7-5" fill="none" stroke="#0f77b8" stroke-width="1.3"/></svg>
      <span>youremail@crestmail.com</span>
    </div>
  </div>
  <div class="footer-brand"><span class="brand-dot"></span><span class="brand-name">Crestway Hub</span></div>
</footer>

<div class="abs footer-bar">
  <div class="legal">Sitemap<span>|</span>FAQ<span>|</span>Privacy Policy</div>
  <div class="copyright">Copyright 2014 · All rights reserved</div>
  <div class="footer-social"><span></span><span></span><span></span><span></span></div>
</div>
</body>
</html>
```